Business Cards Design for the electrical wholesaler: clean bold dynamic :)

We need a business card design that would follow our latest brand guidelines. As an electrical wholesaler we want to bring a fresh look and feel into the industry. The design should be clean bold and dynamic. It should come alive with the renewed energy of our green colour. Our grey colour should keep things balanced and complement the notion of maturity and responsibility. We employ Lato as a corporate font however are not bound by this font and we’re open to interpretation here.

Target Market(s)

Electrical contractors

Industry/Entity Type

Business

Contact Information for Business Card

Logo
Name & Surname: Olena Dovbush
Job Title: Director of Marketing
Email: helen.dovbush@mailvane.example
Cell phone: XXX.XXX.XXXX
Address: 20917 - 87 Ave. Edmonton, AB, Canada. T6K 2R8
Business Phone: 780.555.0187
Website: www.qorvil.example

Font styles to use
Other font styles liked:
• Lato

Requirements
Must have
• Logo & website
Nice to have
• Brand elements - some of them you may find in the attached Brand Guidelines (e.g. three lines on the background signifying "W")

```html
<!DOCTYPE html>
<html lang="en">
<head>
<meta charset="utf-8">
<title>Qorvil Business Card</title>
<link rel="stylesheet" href="https://fonts.googleapis.com/css2?family=Lato:wght@400;700;900&display=swap">
<style>
  :root {
    --backdrop: #262626;
    --grey-dark: #4a4b4d;
    --grey-text: #505154;
    --green: #8cc63f;
    --white: #ffffff;
    --rule: #6d6e70;
  }
  * { margin: 0; padding: 0; box-sizing: border-box; }
  html, body {
    width: 1200px; height: 902px; overflow: hidden;
    background: var(--backdrop);
    font-family: "Lato", sans-serif;
  }
  .canvas { position: relative; width: 1200px; height: 902px; }

  .card {
    position: absolute;
    width: 560px; height: 320px;
    border-radius: 22px;
    overflow: hidden;
  }
  .card--front { left: 50px; top: 110px; background: var(--grey-dark); }
  .card--back  { left: 590px; top: 470px; background: var(--white); }

  .brand { position: absolute; display: flex; align-items: center; gap: 12px; }
  .brand__mark { width: 26px; height: 26px; background: var(--green); }
  .brand__name {
    font-weight: 900; font-size: 58px; line-height: 1; letter-spacing: -1px;
  }
  .brand__tag {
    position: absolute; font-weight: 700; font-size: 10.5px; letter-spacing: 2.4px;
    text-transform: uppercase;
  }

  .card--front .brand { left: 70px; top: 128px; }
  .card--front .brand__name { color: var(--white); }
  .card--front .brand__tag { left: 108px; top: 194px; color: var(--white); }
  .front__web {
    position: absolute; right: 34px; bottom: 30px;
    font-size: 14px; color: var(--white); letter-spacing: 0.5px;
  }

  .card--back .brand { left: 40px; top: 94px; }
  .card--back .brand__name { color: var(--grey-text); }
  .card--back .brand__tag { left: 78px; top: 160px; color: var(--grey-text); }
  .back__rule {
    position: absolute; left: 40px; right: 40px; top: 186px;
    height: 1px; background: var(--rule);
  }

  .person { position: absolute; right: 40px; top: 40px; text-align: right; }
  .person__name { font-weight: 900; font-size: 22px; color: var(--grey-text); }
  .person__title { font-weight: 700; font-size: 14px; color: var(--green); margin-top: 2px; }

  .address {
    position: absolute; right: 40px; top: 100px; text-align: right;
    font-size: 13px; line-height: 1.5; color: var(--grey-text);
  }

  .contacts { position: absolute; left: 40px; top: 206px; list-style: none; }
  .contacts li {
    display: flex; align-items: center; gap: 10px;
    font-size: 15px; color: var(--grey-text); margin-bottom: 8px;
  }
  .contacts .icon {
    width: 20px; height: 20px; border-radius: 4px; background: var(--green);
    display: flex; align-items: center; justify-content: center;
  }
</style>
</head>
<body>
<main class="canvas">

  <section class="card card--front" aria-label="Card front">
    <div class="brand">
      <span class="brand__mark"></span>
      <span class="brand__name">qorvil</span>
    </div>
    <span class="brand__tag">Electrical Wholesalers</span>
    <p class="front__web">www.qorvil.example</p>
  </section>

  <section class="card card--back" aria-label="Card back">
    <div class="brand">
      <span class="brand__mark"></span>
      <span class="brand__name">qorvil</span>
    </div>
    <span class="brand__tag">Electrical Wholesalers</span>

    <div class="person">
      <p class="person__name">Olena Dovbush</p>
      <p class="person__title">Director of Marketing</p>
    </div>

    <p class="address">
      20917 - 87 Ave. Edmonton<br>
      AB, Canada. T6K 2R8<br>
      Direct: 780.555.0187<br>
      www.qorvil.example
    </p>

    <div class="back__rule"></div>

    <ul class="contacts">
      <li>
        <span class="icon">
          <svg width="12" height="9" viewBox="0 0 12 9" aria-hidden="true">
            <rect x="0.5" y="0.5" width="11" height="8" fill="none" stroke="#fff" stroke-width="1.2"/>
            <path d="M0.5 0.5 L6 5 L11.5 0.5" fill="none" stroke="#fff" stroke-width="1.2"/>
          </svg>
        </span>
        helen.dovbush@mailvane.example
      </li>
      <li>
        <span class="icon">
          <svg width="12" height="12" viewBox="0 0 24 24" aria-hidden="true">
            <path fill="#fff" d="M6.6 10.8a15.1 15.1 0 0 0 6.6 6.6l2.2-2.2c.3-.3.7-.4 1-.2 1.1.4 2.3.6 3.6.6.6 0 1 .4 1 1V20c0 .6-.4 1-1 1A17 17 0 0 1 3 4c0-.6.4-1 1-1h3.5c.6 0 1 .4 1 1 0 1.3.2 2.5.6 3.6.1.3 0 .7-.2 1z"/>
          </svg>
        </span>
        000.000.0000
      </li>
    </ul>
  </section>

</main>
</body>
</html>
```